Now Leasing Banner

Looking for a banner that says the following information approx 4' x 30'

Now Leasing Maplewood Terrace 925-318-6054

Target Market(s)

Drive by traffic

Industry/Entity Type

Residential property management

Requirements
Must have
• Clear and readable from a distance

```html
<!DOCTYPE html>
<html lang="en">
<head>
<meta charset="utf-8">
<title>Now Leasing Banners – Maplewood Terrace</title>
<link rel="stylesheet" href="https://fonts.googleapis.com/css2?family=Montserrat:wght@700;800;900&display=swap">
<style>
  :root {
    --page-bg: #ececea;
    --navy: #1f2933;
    --aqua: #12d9d9;
    --aqua-pattern: #1d9c99;
    --sun: #f9e600;
    --sky: #3faec6;
    --sky-pattern: #68bcc0;
    --flame: #e8392f;
    --lemon: #f9e21c;
    --amber-pattern: #f1a51f;
    --white: #ffffff;
  }
  * { box-sizing: border-box; margin: 0; padding: 0; }
  html, body {
    width: 1200px; height: 1200px; overflow: hidden;
    background: var(--page-bg);
    font-family: "Montserrat", Arial, sans-serif;
  }
  .banner-set {
    position: relative; width: 1200px; height: 1200px;
    display: flex; justify-content: center; gap: 85px; padding-top: 45px;
  }
  .banner {
    position: relative; width: 150px; height: 1110px; overflow: hidden;
    background: var(--bg);
  }
  .banner__art { position: absolute; left: 0; top: 0; width: 150px; height: 520px; }
  .banner__headline {
    position: absolute; left: 8px; bottom: 226px;
    writing-mode: vertical-rl; transform: rotate(180deg);
    font-weight: 800; line-height: 0.82; letter-spacing: 1px;
  }
  .headline__now { display: block; font-size: 78px; color: var(--now); }
  .headline__leasing { display: block; font-size: 78px; color: var(--leasing); letter-spacing: 2px; }
  .banner__footer {
    position: absolute; left: 0; bottom: 0; width: 150px; height: 122px;
    background: var(--foot); color: var(--foot-text);
    padding: 30px 0 0 8px; font-weight: 800; font-size: 13.5px; line-height: 1.4;
  }
  .footer__phone { display: block; padding-left: 5px; font-size: 14.5px; }

  .banner--navy { --bg: var(--navy); --pat: var(--aqua-pattern); --dot: var(--white); --now: var(--white); --leasing: var(--aqua); --foot: var(--aqua); --foot-text: var(--navy); }
  .banner--sun { --bg: var(--sun); --pat: var(--sky-pattern); --dot: var(--sky); --now: var(--sky); --leasing: var(--sky); --foot: var(--sky); --foot-text: var(--sun); }
  .banner--flame { --bg: var(--flame); --pat: var(--amber-pattern); --dot: var(--amber-pattern); --now: var(--white); --leasing: var(--white); --foot: var(--lemon); --foot-text: var(--flame); }
</style>
</head>
<body>
<main class="banner-set">

  <section class="banner banner--navy">
    <svg class="banner__art" viewBox="0 0 150 520">
      <polygon role="img" aria-label="Decorative wavy line pattern in aqua" points="8,0 150,273 0,518 0,0" fill="var(--pat)"/>
      <g fill="var(--dot)">
        <circle cx="101" cy="48" r="1.5"/><circle cx="118" cy="48" r="1.5"/>
        <circle cx="101" cy="61" r="1.5"/><circle cx="118" cy="61" r="1.5"/>
        <circle cx="101" cy="74" r="1.5"/><circle cx="118" cy="74" r="1.5"/>
        <circle cx="101" cy="87" r="1.5"/><circle cx="118" cy="87" r="1.5"/>
        <circle cx="101" cy="100" r="1.5"/><circle cx="118" cy="100" r="1.5"/>
        <circle cx="101" cy="113" r="1.5"/><circle cx="118" cy="113" r="1.5"/>
      </g>
    </svg>
    <h1 class="banner__headline"><span class="headline__now">Now</span><span class="headline__leasing">LEASING</span></h1>
    <p class="banner__footer">Maplewood Terrace<span class="footer__phone">925-318-6054</span></p>
  </section>

  <section class="banner banner--sun">
    <svg class="banner__art" viewBox="0 0 150 520">
      <polygon role="img" aria-label="Decorative wavy line pattern in blue and yellow" points="8,0 150,273 0,518 0,0" fill="var(--pat)"/>
      <g fill="var(--dot)">
        <circle cx="101" cy="48" r="1.5"/><circle cx="118" cy="48" r="1.5"/>
        <circle cx="101" cy="61" r="1.5"/><circle cx="118" cy="61" r="1.5"/>
        <circle cx="101" cy="74" r="1.5"/><circle cx="118" cy="74" r="1.5"/>
        <circle cx="101" cy="87" r="1.5"/><circle cx="118" cy="87" r="1.5"/>
        <circle cx="101" cy="100" r="1.5"/><circle cx="118" cy="100" r="1.5"/>
        <circle cx="101" cy="113" r="1.5"/><circle cx="118" cy="113" r="1.5"/>
      </g>
    </svg>
    <h1 class="banner__headline"><span class="headline__now">Now</span><span class="headline__leasing">LEASING</span></h1>
    <p class="banner__footer">Maplewood Terrace<span class="footer__phone">925-318-6054</span></p>
  </section>

  <section class="banner banner--flame">
    <svg class="banner__art" viewBox="0 0 150 520">
      <polygon role="img" aria-label="Decorative wavy line pattern in yellow and red" points="8,0 150,273 0,518 0,0" fill="var(--pat)"/>
      <g fill="var(--dot)">
        <circle cx="101" cy="48" r="1.5"/><circle cx="118" cy="48" r="1.5"/>
        <circle cx="101" cy="61" r="1.5"/><circle cx="118" cy="61" r="1.5"/>
        <circle cx="101" cy="74" r="1.5"/><circle cx="118" cy="74" r="1.5"/>
        <circle cx="101" cy="87" r="1.5"/><circle cx="118" cy="87" r="1.5"/>
        <circle cx="101" cy="100" r="1.5"/><circle cx="118" cy="100" r="1.5"/>
        <circle cx="101" cy="113" r="1.5"/><circle cx="118" cy="113" r="1.5"/>
      </g>
    </svg>
    <h1 class="banner__headline"><span class="headline__now">Now</span><span class="headline__leasing">LEASING</span></h1>
    <p class="banner__footer">Maplewood Terrace<span class="footer__phone">925-318-6054</span></p>
  </section>

</main>
</body>
</html>
```